Restaurant menu redo

i just want my menu identical to the files i provided. 1 take out menu and 1 dine in menu. i already have both designs with all the items typed in a word document. i need both menus done so i can easily update prices and items in the future. They can be done in either word or illustrator format. I don't need a new design just a identical copy of both menus that i can update and change my self. one menu is a double sided takeout quad fold(legal size). and the other is a dine in 3 individual page menu.

Industry/Entity Type

Restaurant

Requirements
Must have
• i must have the ability to easily edit the menu for future menu and price changes.
Nice to have
• I would like the menu to be as close to the original as possible.

```html
<!DOCTYPE html>
<html lang="en">
<head>
<meta charset="utf-8">
<title>Marlowe's Italian Pizzeria – Take-Out Menu</title>
<link rel="stylesheet" href="https://fonts.googleapis.com/css2?family=League+Gothic&family=Oswald:wght@500;600&family=Roboto+Condensed:wght@400;700&display=swap">
<style>
:root{
  --red:#e1252b;
  --green:#5aab3a;
  --green-dark:#3f8f2b;
  --ink:#2b2b2b;
  --muted:#555;
  --parchment:#f7eee3;
  --parchment-deep:#efe1cf;
  --price-grey:#d8d8d8;
  --card-line:#e2e2e2;
  --page:#ffffff;
}
*{box-sizing:border-box;margin:0;padding:0}
html,body{width:1200px;height:1200px;overflow:hidden;background:var(--page)}
body{font-family:"Roboto Condensed","Arial Narrow",sans-serif;color:var(--ink);position:relative}

.menu{position:absolute;left:81px;top:253px;width:1034px;height:670px;background:var(--page);box-shadow:0 0 0 1px #ececec}
.panel{position:absolute;top:0;height:670px;overflow:hidden}
.panel--cover{left:0;width:259px;background:var(--page)}
.panel--salads{left:259px;width:258px}
.panel--stromboli{left:517px;width:259px}
.panel--pasta{left:776px;width:258px}
.panel--salads,.panel--stromboli,.panel--pasta{
  background:radial-gradient(ellipse at 40% 30%,var(--parchment) 0%,var(--parchment-deep) 100%);
  border-left:1px solid #e6d8c6;
}
.abs{position:absolute}

/* cover */
.brand{left:0;width:259px;top:26px;text-align:center}
.brand__name{font-family:"Oswald",sans-serif;font-weight:600;font-size:26px;line-height:1.05;color:var(--ink);display:flex;align-items:center;justify-content:center;gap:7px}
.brand__dot{width:12px;height:12px;border-radius:50%;background:var(--red)}
.brand__sub{font-family:"Oswald",sans-serif;font-weight:600;font-size:26px;color:var(--ink);line-height:1.05}
.brand__web{font-size:10px;color:var(--ink);margin-top:5px}
.tagline{left:0;width:259px;top:106px;text-align:center;font-family:"League Gothic",sans-serif;font-size:25px;line-height:1.1;color:var(--red);white-space:nowrap}
.phone{left:0;width:259px;top:138px;text-align:center;font-family:"League Gothic",sans-serif;font-size:22px;line-height:1.1;color:var(--green)}
.address{left:0;width:259px;top:164px;text-align:center;font-size:8.5px;line-height:1.25;color:var(--muted)}
.rule{left:18px;width:222px;top:189px;height:1px;background:#cfcfcf}
.hours{left:0;width:259px;top:198px;text-align:center;font-size:8.5px;line-height:1.45;color:var(--ink);font-weight:700}
.hero{left:0;top:222px;width:259px;height:224px}
.hero__photo{position:absolute;inset:0;background:radial-gradient(ellipse at 50% 45%,#e78a4a 0%,#c4482a 55%,#8a2e1c 100%)}
.hero svg{position:absolute;inset:0}
.section-title--apps{left:0;width:259px;top:456px;text-align:center;font-family:"League Gothic",sans-serif;font-weight:400;font-size:16px;line-height:1.1;color:var(--red)}

/* headings */
.h{font-family:"League Gothic",sans-serif;font-weight:400;font-size:14px;line-height:1.15;color:var(--red);text-transform:uppercase;letter-spacing:.1px;white-space:nowrap}
.h--green{color:var(--green);font-size:15px;line-height:1.2}

/* menu cards */
.card{display:flex;background:#fff;border:1px solid var(--card-line);font-size:5.6px;line-height:1.45;color:var(--ink)}
.card__desc{flex:1;padding:5px 5px}
.card__price{width:24px;background:var(--price-grey);display:flex;flex-direction:column;justify-content:center;align-items:center;gap:2px}
.card__sizes{display:flex;justify-content:space-between;margin-top:4px}
.list{background:linear-gradient(to left,var(--price-grey) 24px,#fff 24px);border:1px solid var(--card-line);font-size:5.6px;line-height:1.3;padding:4px 0}
.list__row{display:grid;grid-template-columns:1fr 24px;padding:1.6px 0 1.6px 4px}
.list__row span:last-child{text-align:center}
.list--apps{font-size:5.4px}
.list--apps .list__row{padding:1.9px 0 1.9px 4px}

.note{font-size:7.5px;line-height:1.3;color:var(--ink);font-weight:700}

/* wave + plate */
.wave{left:259px;top:500px;width:775px;height:170px}
.plate{right:10px;bottom:4px;width:184px;height:130px;border-radius:50% 50% 46% 46%;background:radial-gradient(ellipse at 55% 45%,#e0402b 0%,#c8302a 30%,#6aa84a 62%,#f4f4f4 82%)}
</style>
</head>
<body>
<main class="menu">

  <!-- Cover panel -->
  <section class="panel panel--cover">
    <div class="abs brand">
      <div class="brand__name"><span class="brand__dot"></span>Marlowe's</div>
      <div class="brand__sub">Italian Pizzeria</div>
      <div class="brand__web">www.marlowespizzeria.biz</div>
    </div>
    <div class="abs tagline">DINE IN · PICK-UP · WE DELIVER!</div>
    <div class="abs phone">555.014.2280</div>
    <div class="abs address">1820 Harbor Blvd.<br>Bayview FL 33000</div>
    <div class="abs rule"></div>
    <div class="abs hours">Mon-Fri 11am-11pm • Sat-Sun 12pm-11pm<br>Restaurant closes at 11pm</div>

    <div class="abs hero">
      <div class="hero__photo" role="img" aria-label="Photo of penne pasta in tomato sauce with basil"></div>
      <svg viewBox="0 0 259 224" preserveAspectRatio="none" aria-hidden="true">
        <path d="M0,0 H259 V30 Q140,-4 0,14 Z" fill="#fff"/>
        <path d="M0,14 Q140,-2 259,30" fill="none" stroke="var(--green)" stroke-width="2.5"/>
        <path d="M0,20 Q140,6 259,38" fill="none" stroke="var(--red)" stroke-width="6"/>
        <path d="M0,184 Q120,230 259,214 V224 H0 Z" fill="#fff"/>
        <path d="M0,182 Q120,228 259,212" fill="none" stroke="var(--red)" stroke-width="6"/>
        <path d="M0,174 Q120,220 259,204" fill="none" stroke="var(--green)" stroke-width="2.5"/>
      </svg>
    </div>

    <h2 class="abs section-title--apps">APPETIZERS</h2>
    <div class="abs list list--apps" style="left:7px;top:481px;width:112px;height:168px">
      <div class="list__row"><span>Calamari Fritto Misto</span><span>9.49</span></div>
      <div class="list__row"><span>Pizza Bread</span><span>4.99</span></div>
      <div class="list__row"><span>Twice Baked Stuffed Clams</span><span>9.49</span></div>
      <div class="list__row"><span>Clam Strips</span><span>7.99</span></div>
      <div class="list__row"><span>Bruschetta</span><span>7.99</span></div>
      <div class="list__row"><span>Clams Bianco or Rosso (red or white)</span><span>11.99</span></div>
      <div class="list__row"><span>Homemade Zucchini Sticks</span><span>7.99</span></div>
      <div class="list__row"><span>Italian Chicken Tenders</span><span>8.49</span></div>
      <div class="list__row"><span>Mussels Marinara or Bianco (red or white)</span><span>10.99</span></div>
      <div class="list__row"><span>Garlic Rolls</span><span>1.25 (6) 4.99 (12) 9.00</span></div>
      <div class="list__row"><span>Broccoli Rabe Rappini</span><span>8.99</span></div>
    </div>
    <div class="abs list list--apps" style="left:129px;top:481px;width:121px;height:168px">
      <div class="list__row"><span>Southern Italian bitter green &amp; roasted garlic, add Sausage</span><span>$3.00</span></div>
      <div class="list__row"><span>Roasted Chicken Wings Slow roasted chicken wings tossed with your choice of sauce, served with bleu cheese &amp; celery.</span><span>(10) 9.49 (20) 17.99</span></div>
      <div class="list__row"><span>Choice of Sauce: Hot Medium Mild Roasted Garlic Parmesan BBQ Jamaican Jerk Greek Style Honey Roasted Garlic Thai Chili</span><span></span></div>
      <div class="list__row"><span>Extra Sauce</span><span>.50</span></div>
      <div class="list__row"><span>Extra Bleu Cheese</span><span>.75</span></div>
      <div class="list__row"><span>Extra Garlic</span><span>.50</span></div>
    </div>
  </section>

  <!-- Sides & salads panel -->
  <section class="panel panel--salads">
    <h3 class="abs h" style="left:10px;top:22px">Sides</h3>
    <div class="abs list" style="left:10px;top:42px;width:104px;height:58px">
      <div class="list__row"><span>Fries</span><span>3.49</span></div>
      <div class="list__row"><span>Caesar Salad</span><span>4.99</span></div>
      <div class="list__row"><span>Pasta Marinara</span><span>4.49</span></div>
      <div class="list__row"><span>Sausage</span><span>3.49</span></div>
    </div>
    <div class="abs list" style="left:131px;top:42px;width:105px;height:58px">
      <div class="list__row"><span>House Side Salad</span><span>3.99</span></div>
      <div class="list__row"><span>Fresh Garden Vegetables</span><span>4.49</span></div>
      <div class="list__row"><span>Meatballs (2)</span><span>4.00</span></div>
      <div class="list__row"><span>Toasted Ciabatta</span><span>2.00</span></div>
    </div>

    <h3 class="abs h" style="left:12px;top:120px">Soup and<br>Salad Creations</h3>
    <div class="abs list" style="left:10px;top:155px;width:104px;height:40px">
      <div class="list__row"><span>Pasta Fagioli</span><span>3.99</span></div>
      <div class="list__row"><span>Soup of the Day</span><span>3.99</span></div>
      <div class="list__row"><span>Coleslaw</span><span>.95</span></div>
    </div>
    <h3 class="abs h" style="left:132px;top:120px">Greek Salad</h3>
    <div class="abs card" style="left:132px;top:139px;width:104px;height:56px">
      <div class="card__desc">Fresh greens, black olives, tomatoes, cucumbers, red onions, pepperoncini, roasted peppers, feta cheese &amp; croutons</div>
      <div class="card__price">9.99</div>
    </div>

    <h3 class="abs h" style="left:12px;top:220px">House</h3>
    <div class="abs card" style="left:12px;top:239px;width:102px;height:56px">
      <div class="card__desc">Fresh greens, black olives, cucumbers, tomatoes, red onions, pepperoncini, pecorino cheese &amp; croutons</div>
      <div class="card__price">7.99</div>
    </div>
    <h3 class="abs h" style="left:132px;top:220px">Caprese</h3>
    <div class="abs card" style="left:132px;top:239px;width:104px;height:56px">
      <div class="card__desc">Fresh tomatoes, basil &amp; buffalo mozzarella drizzled with balsamic vinegar &amp; olive oil, served with ciabatta bread.</div>
      <div class="card__price">9.49</div>
    </div>

    <h3 class="abs h" style="left:12px;top:312px">Caesar</h3>
    <div class="abs card" style="left:12px;top:331px;width:102px;height:56px">
      <div class="card__desc">Fresh cut romaine lettuce, croutons, Caesar dressing &amp; Pecorino cheese, topped with red onions. 8.99</div>
      <div class="card__price">8.99</div>
    </div>
    <h3 class="abs h" style="left:132px;top:312px">The Wedge</h3>
    <div class="abs card" style="left:132px;top:331px;width:104px;height:56px">
      <div class="card__desc">Fresh iceberg lettuce, tomato, topped with homemade bleu cheese, warm bacon &amp; red onions.</div>
      <div class="card__price">8.49</div>
    </div>

    <h3 class="abs h" style="left:12px;top:397px">Caesar</h3>
    <div class="abs card" style="left:12px;top:418px;width:102px;height:54px">
      <div class="card__desc">Fresh cut romaine lettuce, tomato, ham, salami, provolone, black olives, cucumbers, pepperoncini.</div>
      <div class="card__price">8.99</div>
    </div>
    <h3 class="abs h" style="left:134px;top:397px">Add any of the following</h3>
    <div class="abs list" style="left:132px;top:418px;width:104px;height:54px">
      <div class="list__row"><span>Chicken</span><span>4.00</span></div>
      <div class="list__row"><span>Tilapia</span><span>4.00</span></div>
      <div class="list__row"><span>Mahi Mahi</span><span>5.00</span></div>
      <div class="list__row"><span>Shrimp</span><span>5.00</span></div>
    </div>

    <h3 class="abs h" style="left:12px;top:489px">Calzones &amp; Stromboli</h3>
    <div class="abs card" style="left:12px;top:509px;width:102px;height:70px">
      <div class="card__desc">Chicago Calzone<br>A pizza pocket stuffed with ricotta &amp; mozzarella, severed with<br>A side of pizza sauce.<br>Personal</div>
      <div class="card__price"><span>8.49</span><span>Regular</span><span>11.49</span></div>
    </div>
    <p class="abs h h--green" style="left:130px;top:515px">Additional<br>Toppings-See Personal<br>Pizza Toping Price</p>
  </section>

  <!-- Stromboli panel -->
  <section class="panel panel--stromboli">
    <h3 class="abs h" style="left:12px;top:22px">Chicago Stromboli</h3>
    <div class="abs card" style="left:14px;top:43px;width:114px;height:72px">
      <div class="card__desc">Stuffed with pepperoni, Italian sausage, peppers, onions, mushrooms, &amp; mozzarella.<div class="card__sizes"><span>Personal</span></div><div>Regular</div></div>
      <div class="card__price"><span>11.49</span><span>14.49</span></div>
    </div>
    <h3 class="abs h" style="left:137px;top:22px">Veggie Stromboli</h3>
    <div class="abs card" style="left:137px;top:43px;width:115px;height:72px">
      <div class="card__desc">Stuffed with spinach, tomatoes, black olives, peppers, onions, mushrooms, &amp; mozzarella.<div class="card__sizes"><span>Personal</span></div><div>Regular</div></div>
      <div class="card__price"><span>11.49</span><span>14.49</span></div>
    </div>

    <h3 class="abs h" style="left:12px;top:132px">Meat Lovers Stromboli</h3>
    <div class="abs card" style="left:14px;top:158px;width:114px;height:74px">
      <div class="card__desc">Stuffed with meatball, sausage, Canadian ham, pepperoni, bacon, &amp; mozzarella.<div class="card__sizes"><span>Personal</span></div><div>Regular</div></div>
      <div class="card__price"><span>13.49</span><span>15.99</span></div>
    </div>
    <p class="abs note" style="left:137px;top:183px;width:112px">No substitutions on Stromboli, any changes will result in ala carte pricing</p>

    <h3 class="abs h" style="left:14px;top:244px">Pasta Celebrations</h3>
    <div class="abs card" style="left:14px;top:262px;width:114px;height:76px">
      <div class="card__desc">All served with side house salad &amp; garlic roll. Add any of the following to the below pasta dishes: Chicken, Meatballs or<div class="card__sizes"><span>Sausage</span></div><div>Shrimp</div></div>
      <div class="card__price"><span>4.00</span><span>5.00</span></div>
    </div>
    <h3 class="abs h" style="left:134px;top:244px">Linguini Aioli</h3>
    <div class="abs card" style="left:134px;top:264px;width:118px;height:74px">
      <div class="card__desc">Fresh roasted garlic sautéed in olive oil, tossed with linguini &amp; fresh herbs, sea salt &amp; fresh cracked black pepper.</div>
      <div class="card__price">12.49</div>
    </div>

    <h3 class="abs h" style="left:14px;top:360px">Spaghetti ala Marinara Rigatoni ala Vodka</h3>
    <div class="abs card" style="left:14px;top:381px;width:114px;height:40px">
      <div class="card__desc">Homemade marinara sauce tossed with spaghetti.</div>
      <div class="card__price">12.49</div>
    </div>
    <div class="abs card" style="left:134px;top:381px;width:118px;height:50px">
      <div class="card__desc">Sun dried tomatoes, pancetta sautéed, a touch of marinara, cream &amp; a blend of grated cheeses, tossed with rigatoni &amp; fresh basil.</div>
      <div class="card__price">15.99</div>
    </div>

    <h3 class="abs h" style="left:14px;top:442px">Broccoli &amp; Garlic</h3>
    <div class="abs card" style="left:14px;top:463px;width:114px;height:52px">
      <div class="card__desc">Broccoli florets &amp; roasted garlic sautéed in olive oil then tossed with bowtie pasta &amp; a blend of grated cheeses.</div>
      <div class="card__price">15.49</div>
    </div>
  </section>

  <!-- Pasta & seafood panel -->
  <section class="panel panel--pasta">
    <h3 class="abs h" style="left:10px;top:22px">Fettuccine Alfredo</h3>
    <div class="abs card" style="left:12px;top:42px;width:110px;height:52px">
      <div class="card__desc">Warm cream, blended with rich egg yolks &amp; a blend of cheese, tossed in fettuccine.</div>
      <div class="card__price">15.49</div>
    </div>
    <h3 class="abs h" style="left:126px;top:22px">Penne ala Fresca</h3>
    <div class="abs card" style="left:128px;top:42px;width:114px;height:52px">
      <div class="card__desc">Fresh plum tomatoes &amp; basil sautéed in olive oil then tossed with penne pasta, butter &amp; a blend of grated cheeses.</div>
      <div class="card__price">13.99</div>
    </div>

    <h3 class="abs h" style="left:10px;top:115px">Fettuccine Alfredo</h3>
    <div class="abs card" style="left:12px;top:135px;width:110px;height:66px">
      <div class="card__desc">Sweet Italian sausage, assorted peppers &amp; onions sautéed in extra virgin olive oil, tossed with our homemade marinara sauce. Served with a side of pasta.</div>
      <div class="card__price">16.49</div>
    </div>
    <h3 class="abs h" style="left:126px;top:115px">Calamari Fra Diavolo</h3>
    <div class="abs card" style="left:128px;top:135px;width:114px;height:66px">
      <div class="card__desc">Fresh calamari sautéed with our homemade marinara sauce, garlic, white wine, olive oil, and red pepper flakes then tossed with linguini.</div>
      <div class="card__price">17.49</div>
    </div>

    <h3 class="abs h" style="left:10px;top:216px">Linguini with Red or<br>White Clam Sauce</h3>
    <div class="abs card" style="left:12px;top:259px;width:110px;height:60px">
      <div class="card__desc">Hard shell clams &amp; garlic sautéed in olive oil &amp; a splash of white wine &amp; fresh herbs tossed in linguini.</div>
      <div class="card__price">18.49</div>
    </div>
    <h3 class="abs h" style="left:126px;top:216px">Mussels Marinara<br>or Bianco</h3>
    <div class="abs card" style="left:128px;top:259px;width:114px;height:60px">
      <div class="card__desc">Mussels &amp; roasted garlic sautéed in olive oil, a splash of white wine &amp; a touch of marinara sauce tossed with linguini.</div>
      <div class="card__price">17.49</div>
    </div>

    <h3 class="abs h" style="left:10px;top:334px">Sunday Gravy</h3>
    <div class="abs card" style="left:12px;top:359px;width:110px;height:74px">
      <div class="card__desc">Short ribs, pork shoulder, fresh garlic, celery &amp; carrots sautéed in olive oil, with plum crushed tomatoes, served over pappardelle pasta with a side of meatballs &amp; sausage.</div>
      <div class="card__price">17.99</div>
    </div>
    <div class="abs list" style="left:128px;top:359px;width:114px;height:74px">
      <div class="list__row" style="padding-top:4px"><span>Meatballs &amp; sausage</span><span>17.99</span></div>
      <div class="list__row"><span>Baked Lasagna</span><span>13.99</span></div>
      <div class="list__row"><span>Baked Rigatoni</span><span>13.49</span></div>
      <div class="list__row"><span>Baked Manicotti</span><span>13.49</span></div>
      <div class="list__row"><span>Baked Ravioli Dinner</span><span>13.49</span></div>
    </div>

    <h3 class="abs h" style="left:10px;top:440px">Shrimp Scampi</h3>
    <div class="abs card" style="left:12px;top:465px;width:110px;height:50px">
      <div class="card__desc">Succulent shrimp sautéed in a garlic, butter and wine sauce. Served over linguini.</div>
      <div class="card__price">17.49</div>
    </div>
    <h3 class="abs h" style="left:126px;top:440px">Chicken Breast Dinner</h3>
    <div class="abs card" style="left:128px;top:465px;width:114px;height:50px">
      <div class="card__desc">Fresh chicken breast grilled or blackened, served with a side of vegetables &amp; roasted potatoes.</div>
      <div class="card__price">15.49</div>
    </div>
  </section>

  <!-- Bottom band across inner panels -->
  <svg class="abs wave" viewBox="0 0 775 170" preserveAspectRatio="none" aria-hidden="true">
    <path d="M0,96 Q230,150 517,6 L517,86 Q640,64 775,66 L775,170 L0,170 Z" fill="var(--red)"/>
    <path d="M0,106 Q230,160 517,18 L517,96 Q640,76 775,78 L775,170 L0,170 Z" fill="var(--green)"/>
    <path d="M0,130 Q230,170 517,60 L517,170 L0,170 Z" fill="var(--green-dark)" opacity=".35"/>
  </svg>
  <div class="abs plate" role="img" aria-label="Photo of a stuffed tomato salad plate with greens and corn"></div>

</main>
</body>
</html>
```